Educational website design and repeat learning

The aim of the project is to create a learning platform to support high school students in their learning. It aims to integrate as much as possible the potential of digital tools (videos, navigation) in the educational path of students, in the acquisition of knowledge and its use. In particular, it will integrate a learning system in spaced repetition (flashcards).

The students are the central users of the platform. They must have access to the following features:
• Access to course content and the map review tool
• Personal dashboard, retracing the courses taken, the number of revised cards and other metrics
• A notification panel, suggesting to him the revision of such or such pack of cards, or of such or such concept in the rest of the contents

Flashcards are a learning system based on spaced repetition, on a format of cards associating a question and an answer. Ideally, each card involves only a limited amount of knowledge. The learner successively repeats the cards and associates with each of them a difficulty (or failure if necessary), leading the system to offer him, as a priority, the cards that are the most difficult for him.

Once the designer has been chosen, the site map and the wireframes will be transmitted to start work on the site code.
Updates

Les designs se ressemblent

Target Market(s)

High school students - France

Industry/Entity Type

Education

Logo Text

brio-slate

Coding

Coded - Design and coding required

Number of Pages Required

4 page

Font styles to use
Sans Serif

Requirements
Must have
• Must be offered:
- 1 design of home page, content (lorem ipsum), possibility of connection / registration
- 1 course sheet page design, with the complete course hierarchy
- 1 design of the spaced repetition tool
Nice to have
• - 1 student dashboard design with the following elements:
• Time spent on the platform (graph week by week + week in progress)
• Number of course sheets read (total and week)
• Number of cards revised (total and week)
Should not have
• Light blue

```html
<!DOCTYPE html>
<html lang="en">
<head>
<meta charset="utf-8">
<title>Brio-Slate — Learning Platform</title>
<link href="https://fonts.googleapis.com/css2?family=Raleway:wght@600;700;800&family=Arimo:ital,wght@0,400;0,700;1,400&display=swap" rel="stylesheet">
<style>
:root{
  --orange:#fc8f0c;
  --ink:#111;
  --text:#333;
  --muted:#777;
  --light:#999;
  --line:#e6e6e6;
  --dark:#171717;
  --white:#fff;
}
*{box-sizing:border-box;margin:0;padding:0}
html,body{width:1200px;height:3522px;overflow:hidden;background:var(--white)}
body{font-family:"Arimo",Arial,sans-serif;color:var(--text)}
.page{position:relative;width:1200px;height:3522px;overflow:hidden}
.abs{position:absolute}
.head{font-family:"Raleway",sans-serif;font-weight:800;text-transform:uppercase;color:var(--ink)}
.accent{color:var(--orange)}
.diamond{position:absolute;width:56px;height:56px;background:var(--orange);transform:rotate(45deg)}
.photo{position:absolute}
.btn{position:absolute;display:flex;align-items:center;justify-content:center;font-family:"Raleway",sans-serif;font-weight:800;font-size:13px;text-transform:uppercase}
.btn-outline{border:2px solid var(--orange);color:var(--orange);background:var(--white)}
.topline{position:absolute;left:0;top:0;width:1200px;height:3px;background:var(--orange)}

/* header */
.brand{position:absolute;left:110px;top:22px;display:flex;align-items:center;gap:14px}
.brand-mark{width:44px;height:44px;border:3px solid #9a9a9a}
.brand-name{font-family:"Raleway",sans-serif;font-weight:700;font-size:21px;color:#666}
.nav{position:absolute;top:47px;left:594px;display:flex;font-family:"Raleway",sans-serif;font-weight:700;font-size:13px;color:#222}
.nav a{position:absolute;white-space:nowrap;text-decoration:none;color:inherit}
.nav .active{color:var(--orange)}
.nav .active::after{content:"";position:absolute;left:-3px;right:-3px;bottom:-10px;height:3px;background:var(--orange)}

/* hero */
.hero{left:20px;top:103px;width:1160px;height:510px;background:linear-gradient(90deg,#c9cfb8 0%,#d8dccb 35%,#b9a48e 60%,#d9d2c8 85%,#e4e2df 100%)}
.hero-title{position:absolute;left:110px;top:240px;font-size:30px;line-height:42px;width:500px}
.dots{position:absolute;top:482px;left:572px;display:flex;gap:8px}
.dots span{width:12px;height:12px;border-radius:50%;background:#fff;border:1px solid #ddd}

/* features */
.features{position:absolute;left:111px;top:530px;width:978px;height:208px;background:#fff;box-shadow:0 2px 12px rgba(0,0,0,.12);display:flex}
.feature{flex:1;text-align:center;padding-top:34px}
.feature svg{width:72px;height:72px}
.feature p{margin-top:20px;font-size:19px;line-height:26px;color:#555}

/* section headings */
.sec-title{position:absolute;left:0;width:1200px;text-align:center;font-size:34px}
.sec-sub{position:absolute;left:0;width:1200px;text-align:center;font-size:13.5px;line-height:26px;color:#666}

/* course cards */
.card{position:absolute;top:946px;width:316px;height:382px;background:#fff;box-shadow:0 1px 8px rgba(0,0,0,.14)}
.card .photo{left:0;top:0;width:316px;height:193px}
.card-body{position:absolute;left:28px;right:28px;top:216px}
.card h3{font-family:"Raleway",sans-serif;font-weight:800;font-size:16.5px;line-height:26px;text-transform:uppercase;color:#111}
.card .desc{margin-top:10px;font-size:13.5px;line-height:26px;color:#999}
.card .meta{margin-top:10px;display:flex;justify-content:space-between;font-size:13.5px;color:#999}
.card .meta b{font-family:"Raleway",sans-serif;font-weight:800;color:var(--orange);font-size:13.5px}

/* serve */
.serve-title{position:absolute;left:630px;top:1558px;font-size:34px}
.body-copy{position:absolute;font-size:14px;line-height:25.5px;color:#666;text-align:justify}
.play{position:absolute;left:322px;top:1637px;width:58px;height:58px;border-radius:50%;background:#fff;display:flex;align-items:center;justify-content:center}

/* client */
.quote{position:absolute;left:111px;top:2071px;width:452px;font-style:italic;font-size:14px;line-height:25.5px;color:#666;text-align:justify}
.author{position:absolute;left:111px;top:2182px;font-family:"Arimo",sans-serif;font-weight:700;font-size:14px;letter-spacing:3.5px;color:#111}
.arrow-btn{position:absolute;width:57px;height:57px;display:flex;align-items:center;justify-content:center}

/* blog */
.post{position:absolute;top:2470px;width:317px;text-align:center}
.post .photo{position:relative;width:317px;height:197px}
.post .date{margin-top:18px;font-size:14px;letter-spacing:4px;color:#999}
.post h3{margin-top:9px;font-family:"Raleway",sans-serif;font-weight:800;font-size:18.5px;color:#111;text-transform:uppercase}
.post .desc{margin-top:8px;font-size:14px;line-height:21px;color:#888}
.post .meta{margin-top:16px;display:flex;justify-content:center;gap:32px;font-size:14px;color:#222}
.post .meta span{display:flex;align-items:center;gap:4px}
.side-btn{position:absolute;top:2645px;width:56px;height:56px;background:#efefef;display:flex;align-items:center;justify-content:center}

/* footer */
.footer{position:absolute;left:20px;top:2920px;width:1160px;height:602px;background:var(--dark);color:#fff}
.nl-title{position:absolute;left:0;top:88px;width:1160px;text-align:center;font-family:"Raleway",sans-serif;font-weight:700;font-size:22px}
.nl-sub{position:absolute;left:0;top:124px;width:1160px;text-align:center;font-size:13.5px}
.nl-input{position:absolute;left:388px;top:154px;width:385px;height:44px;background:#fff;color:#888;font-size:13.5px;padding:14px 16px}
.nl-check{position:absolute;left:0;top:214px;width:1160px;text-align:center;font-size:13.5px}
.nl-check i{display:inline-block;width:11px;height:11px;border:1px solid #fff;margin-right:4px;vertical-align:-1px}
.nl-btn{position:absolute;left:505px;top:250px;width:151px;height:40px;background:var(--orange);display:flex;align-items:center;justify-content:center;font-weight:700;font-size:14px;letter-spacing:4px}
.col{position:absolute;top:350px}
.col h4{font-family:"Raleway",sans-serif;font-weight:700;font-size:21px;text-transform:uppercase;margin-bottom:16px}
.col li{list-style:none;font-size:13.5px;line-height:25.6px}
.col.social li{color:var(--orange)}
.f-rule{position:absolute;left:128px;top:538px;width:904px;height:1px;background:#555}
.copy{position:absolute;left:0;top:558px;width:1160px;text-align:center;font-size:13.5px}
</style>
</head>
<body>
<div class="page">
  <div class="topline"></div>

  <!-- header -->
  <div class="brand">
    <div class="brand-mark"></div>
    <div class="brand-name">brio-slate</div>
  </div>
  <nav class="nav">
    <a class="active" style="left:0">HOME</a>
    <a style="left:70px">ABOUT US</a>
    <a style="left:171px">SERVICES</a>
    <a style="left:270px">COURSES</a>
    <a style="left:364px">CONTACT US</a>
    <svg style="position:absolute;left:482px;top:1px" width="14" height="14" viewBox="0 0 14 14"><circle cx="6" cy="6" r="4.5" fill="none" stroke="#222" stroke-width="2"/><line x1="9.3" y1="9.3" x2="13" y2="13" stroke="#222" stroke-width="2"/></svg>
  </nav>

  <div class="diamond" style="left:-22px;top:75px;width:50px;height:50px"></div>

  <!-- hero -->
  <div class="photo hero" role="img" aria-label="Smiling high school student sitting at a laptop in a bright study room"></div>
  <h1 class="head hero-title">Learning platform to support high school students in their learning</h1>
  <div class="btn" style="left:111px;top:384px;width:124px;height:44px;border:2px solid #111;background:#fff;color:#111">Learn more</div>
  <div class="btn" style="left:248px;top:384px;width:125px;height:44px;background:var(--orange);color:#fff">Play video</div>
  <div class="dots"><span></span><span></span><span></span></div>

  <!-- features -->
  <div class="features">
    <div class="feature">
      <svg viewBox="0 0 72 72" fill="none" stroke="#777" stroke-width="2"><circle cx="36" cy="30" r="20"/><circle cx="36" cy="30" r="14"/><path d="M36 22l2.6 5.3 5.8.8-4.2 4.1 1 5.8-5.2-2.7-5.2 2.7 1-5.8-4.2-4.1 5.8-.8z"/><path d="M24 46l-6 18 8-3 4 7 5-18M48 46l6 18-8-3-4 7-5-18"/></svg>
      <p>Certification</p>
    </div>
    <div class="feature">
      <svg viewBox="0 0 72 72" fill="none" stroke="#777" stroke-width="2"><rect x="10" y="20" width="44" height="32"/><path d="M4 58h58l-4-6H8z"/><rect x="40" y="6" width="26" height="26" fill="#fff"/><path d="M46 12h5v5h-5zM55 12h5v5h-5zM46 21h5v5h-5zM55 21h5v5h-5z"/><path d="M20 36l10-5 10 5-10 5z"/></svg>
      <p>Teaching Materials</p>
    </div>
    <div class="feature">
      <svg viewBox="0 0 72 72" fill="none" stroke="#777" stroke-width="2"><path d="M8 62l16-18 12 10 22-26"/><path d="M48 26h10v10"/><path d="M8 62h56"/></svg>
      <p>Career Upgrade</p>
    </div>
    <div class="feature">
      <svg viewBox="0 0 72 72" fill="none" stroke="#777" stroke-width="2"><path d="M20 14h32l10 12-26 26-26-26z"/><path d="M10 26h52M28 14l-4 12 12 26 12-26-4-12"/><path d="M14 56h44v6H14z"/></svg>
      <p>Superior<br>Accomodation</p>
    </div>
  </div>

  <div class="diamond" style="left:1162px;top:703px;width:50px;height:50px"></div>

  <!-- courses -->
  <h2 class="head sec-title" style="top:820px">Our <span class="accent">Cources</span></h2>
  <p class="sec-sub" style="top:874px">Lorem ipsum dolor sit amet, consectetur adipiscing elit, sed do eiusmod tempor incididunt ut labore et dolore magna<br>aliqua. Ut enim ad minim veniam, quis nostrud exercitation ullamco laboris</p>

  <div class="diamond" style="left:87px;top:927px;width:48px;height:48px"></div>

  <article class="card" style="left:111px">
    <div class="photo" role="img" aria-label="Teacher helping a group of students working at computers" style="background:linear-gradient(135deg,#cfd6d8,#8c8378 55%,#b7a08e)"></div>
    <div class="card-body">
      <h3>Lorem ipsum dolor sit amet consectetur</h3>
      <p class="desc">Lorem ipsum dolor sit amet, conse&nbsp;&nbsp;cte tur adipiscing</p>
      <div class="meta"><span>512 Views</span><b>View more</b></div>
    </div>
  </article>
  <article class="card" style="left:442px">
    <div class="photo" role="img" aria-label="Student with headphones writing notes beside a laptop" style="background:linear-gradient(135deg,#ececec,#d7d3cf 50%,#6d6460)"></div>
    <div class="card-body">
      <h3>Lorem ipsum dolor sit amet consectetur</h3>
      <p class="desc">Lorem ipsum dolor sit amet, conse&nbsp;&nbsp;cte tur adipiscing</p>
      <div class="meta"><span>512 Views</span><b>View more</b></div>
    </div>
  </article>
  <article class="card" style="left:773px">
    <div class="photo" role="img" aria-label="Students studying together at a classroom table" style="background:linear-gradient(135deg,#9a9288,#3f7d86 45%,#d6dbdb)"></div>
    <div class="card-body">
      <h3>Lorem ipsum dolor sit amet consectetur</h3>
      <p class="desc">Lorem ipsum dolor sit amet, conse&nbsp;&nbsp;cte tur adipiscing</p>
      <div class="meta"><span>512 Views</span><b>View more</b></div>
    </div>
  </article>

  <svg class="abs" style="left:1068px;top:1292px" width="60" height="62" viewBox="0 0 60 62"><path d="M30 0l30 31-30 31-8-8 4-18H2z" fill="#000"/></svg>

  <div class="btn btn-outline" style="left:503px;top:1362px;width:194px;height:43px">View more courses</div>

  <!-- serve -->
  <div class="diamond" style="left:90px;top:1484px;width:48px;height:48px"></div>
  <div class="photo" role="img" aria-label="Two students smiling while working together on a laptop" style="left:111px;top:1501px;width:477px;height:361px;background:linear-gradient(135deg,#c9a58a,#e6d9c8 45%,#7e6a5a 80%,#d8cfc4)"></div>
  <div class="play"><svg width="14" height="16" viewBox="0 0 14 16"><path d="M2 1l11 7-11 7z" fill="var(--orange)"/></svg></div>

  <h2 class="head serve-title">How can <span class="accent">we serve you?</span></h2>
  <p class="body-copy" style="left:630px;top:1612px;width:458px">Lorem ipsum dolor sit amet, consectetur adipiscing elit, sed do eiusmod tempor incididunt ut labore et dolore magna aliqua. Ut enim ad minim veniam, quis nostrud exercitation ullamco laboris nisi ut aliquip ex ea commodo consequat. Duis aute irure dolor in</p>
  <div class="btn btn-outline" style="left:631px;top:1742px;width:195px;height:43px">Services request</div>
  <div class="btn btn-outline" style="left:839px;top:1742px;width:194px;height:43px">Ask a question</div>

  <svg class="abs" style="left:1110px;top:1650px" width="90" height="180" viewBox="0 0 90 180" fill="none">
    <g stroke="var(--orange)" stroke-width="2"><path d="M30 12a10 10 0 0 1 6 18v6h-12v-6a10 10 0 0 1 6-18z"/><path d="M26 40h8M14 20h-6M46 20h6M18 6l-4-4M42 6l4-4"/></g>
    <path d="M30 52c0 50 20 90 60 128" stroke="#bbb" stroke-width="1.5" stroke-dasharray="6 5"/>
  </svg>

  <!-- client words -->
  <div class="diamond" style="left:1070px;top:1940px;width:50px;height:50px"></div>
  <div class="photo" role="img" aria-label="Student giving a thumbs up in a classroom" style="left:611px;top:1957px;width:477px;height:362px;background:linear-gradient(120deg,#a9b58a,#cfd0c6 40%,#9b8a7e 65%,#e3e2df)"></div>

  <h2 class="head abs" style="left:111px;top:2016px;font-size:34px">Our <span class="accent">Client words</span></h2>
  <p class="quote">“Lorem ipsum dolor sit amet, consectetur adipiscing elit, sed do eiusmod tempor incididunt ut labore et dolore magna aliqua. Ut enim ad minim veniam, quis nostrud exercitation ullamco laboris nisi ut aliquip ex ea commodo consequat.”</p>
  <p class="author">JANE ROE, COMPANY NAME</p>
  <div class="arrow-btn" style="left:111px;top:2228px;background:#e6e6e6"><svg width="14" height="12" viewBox="0 0 14 12"><path d="M6 1L1 6l5 5M1 6h12" stroke="#555" stroke-width="2.4" fill="none"/></svg></div>
  <div class="arrow-btn" style="left:173px;top:2228px;background:var(--orange)"><svg width="14" height="12" viewBox="0 0 14 12"><path d="M8 1l5 5-5 5M13 6H1" stroke="#fff" stroke-width="2.4" fill="none"/></svg></div>

  <svg class="abs" style="left:0;top:2150px" width="70" height="160" viewBox="0 0 70 160" fill="none">
    <g stroke="var(--orange)" stroke-width="2"><path d="M30 10h24a4 4 0 0 1 4 4v12a4 4 0 0 1-4 4H40l-8 6v-6h-2a4 4 0 0 1-4-4V14a4 4 0 0 1 4-4z"/><path d="M33 18h18M33 23h14"/></g>
    <path d="M46 42c4 50-10 90-46 116" stroke="#bbb" stroke-width="1.5" stroke-dasharray="6 5"/>
  </svg>

  <!-- blog -->
  <h2 class="head sec-title" style="top:2402px">Brio-slate <span class="accent">Blog posts</span></h2>

  <div class="side-btn" style="left:26px"><svg width="14" height="12" viewBox="0 0 14 12"><path d="M6 1L1 6l5 5M1 6h12" stroke="#555" stroke-width="2.4" fill="none"/></svg></div>
  <div class="side-btn" style="left:1118px"><svg width="14" height="12" viewBox="0 0 14 12"><path d="M8 1l5 5-5 5M13 6H1" stroke="#555" stroke-width="2.4" fill="none"/></svg></div>

  <article class="post" style="left:111px">
    <div class="photo" role="img" aria-label="Two students laughing while studying with a laptop" style="background:linear-gradient(135deg,#d8c9b6,#8a6d58 50%,#cfc7bd)"></div>
    <p class="date">JUNE 5, 2020</p>
    <h3>Lorem ipsum dolor sit</h3>
    <p class="desc">Lorem ipsum dolor sit amet, consr adipiscing<br>elit. Praesent vestibulum molestie lacus.</p>
    <div class="meta"><span><svg width="14" height="14" viewBox="0 0 14 14"><circle cx="7" cy="7" r="6" fill="none" stroke="#222" stroke-width="1.5"/><circle cx="7" cy="5.5" r="2" fill="#222"/><path d="M3.5 11a4 4 0 0 1 7 0" fill="#222"/></svg>Nora Vale</span><span><svg width="16" height="10" viewBox="0 0 16 10"><path d="M1 5c3-5 11-5 14 0-3 5-11 5-14 0z" fill="#222"/><circle cx="8" cy="5" r="2" fill="#fff"/></svg>521</span><span><svg width="14" height="12" viewBox="0 0 14 12"><path d="M2 1h10v7H6l-3 3V8H2z" fill="none" stroke="#222" stroke-width="1.5"/></svg>3</span></div>
  </article>
  <article class="post" style="left:441px">
    <div class="photo" role="img" aria-label="Laptop showing an online lesson on a desk with supplies" style="background:linear-gradient(135deg,#e7dfd3,#5c5a5c 50%,#d2b79a)"></div>
    <p class="date">JUNE 5, 2020</p>
    <h3>Lorem ipsum dolor sit</h3>
    <p class="desc">Lorem ipsum dolor sit amet, consr adipiscing<br>elit. Praesent vestibulum molestie lacus.</p>
    <div class="meta"><span><svg width="14" height="14" viewBox="0 0 14 14"><circle cx="7" cy="7" r="6" fill="none" stroke="#222" stroke-width="1.5"/><circle cx="7" cy="5.5" r="2" fill="#222"/><path d="M3.5 11a4 4 0 0 1 7 0" fill="#222"/></svg>Nora Vale</span><span><svg width="16" height="10" viewBox="0 0 16 10"><path d="M1 5c3-5 11-5 14 0-3 5-11 5-14 0z" fill="#222"/><circle cx="8" cy="5" r="2" fill="#fff"/></svg>521</span><span><svg width="14" height="12" viewBox="0 0 14 12"><path d="M2 1h10v7H6l-3 3V8H2z" fill="none" stroke="#222" stroke-width="1.5"/></svg>3</span></div>
  </article>
  <article class="post" style="left:772px">
    <div class="photo" role="img" aria-label="Student with headphones studying at a desk" style="background:linear-gradient(135deg,#d9d3c9,#b8ada2 50%,#8a7562)"></div>
    <p class="date">JUNE 5, 2020</p>
    <h3>Lorem ipsum dolor sit</h3>
    <p class="desc">Lorem ipsum dolor sit amet, consr adipiscing<br>elit. Praesent vestibulum molestie lacus.</p>
    <div class="meta"><span><svg width="14" height="14" viewBox="0 0 14 14"><circle cx="7" cy="7" r="6" fill="none" stroke="#222" stroke-width="1.5"/><circle cx="7" cy="5.5" r="2" fill="#222"/><path d="M3.5 11a4 4 0 0 1 7 0" fill="#222"/></svg>Nora Vale</span><span><svg width="16" height="10" viewBox="0 0 16 10"><path d="M1 5c3-5 11-5 14 0-3 5-11 5-14 0z" fill="#222"/><circle cx="8" cy="5" r="2" fill="#fff"/></svg>521</span><span><svg width="14" height="12" viewBox="0 0 14 12"><path d="M2 1h10v7H6l-3 3V8H2z" fill="none" stroke="#222" stroke-width="1.5"/></svg>3</span></div>
  </article>

  <!-- footer -->
  <div class="diamond" style="left:-22px;top:2895px;width:50px;height:50px"></div>
  <footer class="footer">
    <h3 class="nl-title">NEWSLETTER</h3>
    <p class="nl-sub">Get the Latest News and Special Offers</p>
    <div class="nl-input">Email Address</div>
    <p class="nl-check"><i></i>I have read and agree to the terms &amp; conditions</p>
    <div class="nl-btn">SIGN UP</div>

    <div class="col" style="left:149px"><h4>Conditions</h4><ul><li>For Semester Courses</li><li>For 3-week Intensive Course</li><li>For Intensive Summer Courses</li><li>For Individual Courses</li></ul></div>
    <div class="col" style="left:452px"><h4>Menu</h4><ul><li>About Us</li><li>Courses</li><li>Gallery</li><li>FAQ</li><li>Contacts</li></ul></div>
    <div class="col" style="left:671px"><h4>Useful info</h4><ul><li>Working with Us</li><li>Social Programme</li><li>Testimonials</li><li>Student Handbook</li><li>Study Guide</li></ul></div>
    <div class="col social" style="left:932px"><h4>Social</h4><ul><li>Chatterbox</li><li>Snapfolio</li><li>Chirpline</li></ul></div>

    <div class="f-rule"></div>
    <p class="copy">© Copyrights 2020 Brio-Slate | All Rights Reserved</p>
  </footer>
</div>
</body>
</html>
```